Manuka honey wholesales and exports

We need business cards for our honey distribution company based in New Zealand. We supply shops locally and export Manuka honey around the world.
We deal with a very high quality and 100% natural product that can be used for medical, general health as well as food. We are looking business cards that show our honey products are of a high quality with a modern look.

Target Market(s)

Health and medical retailers and importers

Industry/Entity Type

Wholesale

Contact Information for Business Card

Tevin Apiary NZ Limited

www.tevinapiarynz.example

Derek Fawley

M +64 219036482

E tevinapiarynz@mailbox.example

PO Box 58-214
Takapuna
North Shore
Auckland
New Zealand

Font styles to use
Serif

Requirements
Must have
• (Tevin Apiary NZ Limited) with some artwork on one side and all details on the other side.
Nice to have
• I have seen a very simple card with large yellow and black stripes on one side with a company name.. looked clean and simple so something similar or just let the creative beast inside you take over and we will see what you can come up with.

```html
<!DOCTYPE html>
<html lang="en">
<head>
<meta charset="utf-8">
<title>Tevin Apiary NZ Limited – Business Cards</title>
<link href="https://fonts.googleapis.com/css2?family=Open+Sans:wght@400;700&display=swap" rel="stylesheet">
<style>
  :root {
    --backdrop: #d9d9d9;
    --card: #ffffff;
    --honey: #e8901f;
    --bark: #7b3f17;
    --ink: #111111;
    --shade: rgba(0,0,0,0.18);
  }
  * { margin: 0; padding: 0; box-sizing: border-box; }
  html, body {
    width: 1200px; height: 1200px; overflow: hidden;
    background: var(--backdrop);
    font-family: "Open Sans", sans-serif;
  }
  .sheet { position: relative; width: 1200px; height: 1200px; }
  .card {
    position: absolute; left: 100px; width: 1000px; height: 540px;
    background: var(--card); overflow: hidden;
    box-shadow: 0 8px 24px var(--shade);
  }
  .card--front { top: 40px; }
  .card--back { top: 620px; }

  .card__stripes { position: absolute; inset: 0; width: 100%; height: 100%; }

  .brand {
    position: absolute; display: flex; flex-direction: column; align-items: center;
    gap: 18px; width: 320px;
  }
  .card--front .brand { left: 340px; top: 70px; }
  .card--back .brand { left: 60px; top: 150px; }
  .brand__dot {
    width: 120px; height: 120px; border-radius: 50%; background: var(--honey);
  }
  .brand__name {
    font-weight: 700; font-size: 30px; line-height: 1.2; text-align: center;
    color: var(--bark);
  }

  .contact { position: absolute; left: 480px; top: 120px; color: var(--ink); }
  .contact__name {
    font-weight: 700; font-size: 40px; margin-bottom: 26px; letter-spacing: 0.3px;
  }
  .contact__list { list-style: none; }
  .contact__item {
    display: flex; align-items: flex-start; gap: 22px;
    font-size: 24px; line-height: 1.3; margin-bottom: 10px;
  }
  .contact__icon { width: 24px; height: 24px; flex: none; margin-top: 4px; }
  .contact__icon * { fill: none; stroke: var(--honey); stroke-width: 2; }
  .contact__icon .solid { fill: var(--honey); stroke: none; }
</style>
</head>
<body>
<main class="sheet">

  <section class="card card--front" aria-label="Card front">
    <svg class="card__stripes" viewBox="0 0 1000 540" preserveAspectRatio="none" aria-hidden="true">
      <polygon points="0,440 1000,458 1000,484 0,466" fill="var(--bark)"/>
      <polygon points="0,488 1000,500 1000,540 0,528" fill="var(--honey)"/>
    </svg>
    <div class="brand">
      <div class="brand__dot"></div>
      <div class="brand__name">Tevin Apiary<br>NZ Limited</div>
    </div>
  </section>

  <section class="card card--back" aria-label="Card back">
    <div class="brand">
      <div class="brand__dot"></div>
      <div class="brand__name">Tevin Apiary<br>NZ Limited</div>
    </div>

    <div class="contact">
      <h1 class="contact__name">Derek Fawley</h1>
      <ul class="contact__list">
        <li class="contact__item">
          <svg class="contact__icon" viewBox="0 0 24 24" aria-hidden="true">
            <rect x="6" y="2" width="12" height="20" rx="2"/><line x1="10" y1="18" x2="14" y2="18"/>
          </svg>
          <span>+64 219036482</span>
        </li>
        <li class="contact__item">
          <svg class="contact__icon" viewBox="0 0 24 24" aria-hidden="true">
            <rect x="2" y="5" width="20" height="14"/><polyline points="2,5 12,13 22,5"/>
          </svg>
          <span>tevinapiarynz@mailbox.example</span>
        </li>
        <li class="contact__item">
          <svg class="contact__icon" viewBox="0 0 24 24" aria-hidden="true">
            <path class="solid" d="M12 1a7 7 0 0 0-7 7c0 5.5 7 15 7 15s7-9.5 7-15a7 7 0 0 0-7-7zm0 10a3 3 0 1 1 0-6 3 3 0 0 1 0 6z"/>
          </svg>
          <span>PO Box 58-214, Takapuna<br>North Shore, Auckland, New Zealand</span>
        </li>
        <li class="contact__item">
          <svg class="contact__icon" viewBox="0 0 24 24" aria-hidden="true">
            <circle cx="12" cy="12" r="10"/><ellipse cx="12" cy="12" rx="4" ry="10"/>
            <line x1="2" y1="12" x2="22" y2="12"/>
          </svg>
          <span>www.tevinapiarynz.example</span>
        </li>
      </ul>
    </div>
  </section>

</main>
</body>
</html>
```